Need Bold and Innovative Book Cover

Hi,

I am in need of a bold and innovative book cover to catch the attention of people.

Here is what the book is about:

Title: Quiet Harvest - Taming Clutter To Build Your Calmest Season Yet

Author: Captain Dale Farrow

This book is about how to eliminate overwhelm, stress, and information overload from your life. This book is a guide to teach people how I made my life better by getting rid of all kinds of stress, overwhelm, etc.

I have an information product that we created the book from. You can watch the video here to have an even better idea.

http://quietharvestbook.example/

In addition here is an instructional video about what I would like to see for the cover.

http://clipvault.example/t/QpRtZkLmWvA

I look forward to the designs.

Thanks!
Updates

Project Deadline Extended
Reason: Several designers needed a bit more time.

Project Deadline Extended
Reason: Need more time to work on this. Dale

Target Market(s)

Busy people who want to get more done.

Industry/Entity Type

Product

Requirements
Must have
• Model the info product so it all ties in but also use your own creativity.

```html
<!DOCTYPE html>
<html lang="en">
<head>
<meta charset="utf-8">
<title>Quiet Harvest – Book Cover</title>
<link rel="stylesheet" href="https://fonts.googleapis.com/css2?family=Anton&family=Cinzel:wght@600;700&display=swap">
<style>
  :root {
    --page: #ffffff;
    --cover-blue: #04267f;
    --title-red: #e0040c;
    --title-dark: #1a0606;
    --rule-grey: #5a5d6e;
    --ink-white: #ffffff;
    --glow-white: #ffffff;
    --glow-edge: #d9d2c8;
  }
  * { margin: 0; padding: 0; box-sizing: border-box; }
  html, body {
    width: 1000px; height: 1200px; overflow: hidden;
    background: var(--page);
  }
  .canvas { position: relative; width: 1000px; height: 1200px; }
  .cover {
    position: absolute; left: 162px; top: 121px;
    width: 650px; height: 975px;
    background: var(--cover-blue);
    overflow: hidden;
  }
  .title {
    position: absolute; right: 34px; top: 10px;
    text-align: right;
    font-family: "Anton", "Arial Narrow", sans-serif;
    text-transform: uppercase;
    line-height: 1;
  }
  .title-line {
    display: block;
    font-size: 150px;
    letter-spacing: 4px;
    height: 128px;
    line-height: 150px;
    color: var(--title-red);
  }
  .title-line--first { color: var(--title-red); }
  .title-line--second {
    background: linear-gradient(to bottom, var(--title-red) 25%, var(--title-dark) 95%);
    -webkit-background-clip: text; background-clip: text;
    color: transparent;
  }
  .rule {
    position: absolute; height: 2px; background: var(--rule-grey);
  }
  .rule--top { left: 135px; top: 292px; width: 378px; }
  .rule--bottom { left: 140px; top: 384px; width: 378px; }
  .subtitle {
    position: absolute; left: 0; top: 298px; width: 650px;
    text-align: center;
    font-family: "Cinzel", "Times New Roman", serif;
    font-weight: 600;
    color: var(--ink-white);
    font-size: 44px; line-height: 46px;
    text-shadow: 2px 3px 4px rgba(0,0,0,0.6);
  }
  .subtitle-line { display: block; white-space: nowrap; }
  .subtitle-line--first { padding-left: 0; }
  .subtitle-line--second { font-size: 42px; }
  .doorway-scene {
    position: absolute; left: 200px; top: 400px;
    width: 250px; height: 490px;
    background: radial-gradient(ellipse 45% 48% at 50% 50%,
      var(--glow-white) 0%, var(--glow-white) 55%,
      var(--glow-edge) 68%, rgba(4,38,127,0) 100%);
  }
  .author {
    position: absolute; left: 0; top: 915px; width: 650px;
    text-align: center;
    font-family: "Cinzel", "Times New Roman", serif;
    font-weight: 700;
    font-size: 36px; letter-spacing: 4px;
    color: var(--ink-white);
    text-shadow: 2px 3px 4px rgba(0,0,0,0.6);
  }
</style>
</head>
<body>
<main class="canvas">
  <section class="cover">
    <h1 class="title">
      <span class="title-line title-line--first">Quiet</span>
      <span class="title-line title-line--second">Harvest</span>
    </h1>
    <div class="rule rule--top"></div>
    <h2 class="subtitle">
      <span class="subtitle-line subtitle-line--first">Taming Clutter To</span>
      <span class="subtitle-line subtitle-line--second">Build Your Calmest Season</span>
    </h2>
    <div class="rule rule--bottom"></div>
    <div class="doorway-scene" role="img" aria-label="Photo of a man in a suit seen from behind, walking toward a bright glowing doorway"></div>
    <p class="author">Captain Dale Farrow</p>
  </section>
</main>
</body>
</html>
```